Medical marijuana farm

I need a professional looking letterhead for my incorporated company

VERA-LUMO Inc.

"Quiet Birch Farm"

I want the name "Vera lumo" done in a lime green colour, with a black background.... Also- instead of a hyphen I would like a creative "+" sign....

4871 maple street, Nova Scotia is the civic address

902-555-0148

```html
<!DOCTYPE html>
<html lang="en">
<head>
<meta charset="utf-8">
<title>Vera Lumo Letterhead</title>
<link href="https://fonts.googleapis.com/css2?family=Roboto:wght@400;700;900&display=swap" rel="stylesheet">
<style>
  :root {
    --paper: #ffffff;
    --ink: #1b1b1b;
    --lime: #7cc242;
    --brand-bg: #0d0d0d;
    --leaf-light: #e6f3cf;
    --leaf-mid: #bfe08e;
    --leaf-deep: #8fc85a;
  }
  html, body {
    margin: 0;
    padding: 0;
    overflow: hidden;
    background: var(--paper);
  }
  .letterhead {
    position: relative;
    width: 885px;
    height: 1200px;
    background: var(--paper);
    overflow: hidden;
    font-family: "Roboto", Arial, sans-serif;
  }
  .brand-block {
    position: absolute;
    left: 41px;
    top: 0;
    width: 334px;
    height: 97px;
    background: var(--brand-bg);
    display: flex;
    align-items: center;
    justify-content: center;
  }
  .brand-name {
    color: var(--lime);
    font-weight: 900;
    font-size: 60px;
    letter-spacing: -1px;
    line-height: 1;
  }
  .sender {
    position: absolute;
    left: 393px;
    top: 20px;
    font-size: 14px;
    line-height: 22px;
    color: var(--ink);
    font-weight: 700;
  }
  .sender .farm-name {
    color: var(--lime);
  }
  .sender p { margin: 0; }
  .leaf-field {
    position: absolute;
    left: 0;
    top: 0;
    width: 885px;
    height: 1200px;
  }
</style>
</head>
<body>
  <div class="letterhead">
    <div class="brand-block">
      <span class="brand-name">Vera lumo</span>
    </div>

    <div class="sender">
      <p class="farm-name">Quiet Birch Farm</p>
      <p>4871 Maple Street</p>
      <p>Nova Scotia</p>
    </div>

    <svg class="leaf-field" viewBox="0 0 885 1200" role="img" aria-label="Stepped panel of pale green leaf pattern">
      <defs>
        <linearGradient id="leafTone" x1="0" y1="0" x2="1" y2="1">
          <stop offset="0" stop-color="var(--leaf-light)"/>
          <stop offset="0.55" stop-color="var(--leaf-mid)"/>
          <stop offset="1" stop-color="var(--leaf-deep)"/>
        </linearGradient>
      </defs>
      <polygon fill="url(#leafTone)"
        points="885,413 817,413 817,520 610,520 610,708 315,708 315,914 89,914 89,1200 885,1200"/>
      <rect x="620" y="767" width="90" height="135" fill="var(--paper)"/>
      <rect x="210" y="1010" width="90" height="80" fill="var(--paper)"/>
    </svg>
  </div>
</body>
</html>
```